Education business partners flyer

Our service is New Zealand education and migration. We are trying to recruit business partners from around the world who can refer clients to us. We need a 2-3 page PDF flyer that we want to share with our prospective partners. Our content is ready (file attached). It needs to be designed well with relevant NZ images, international students/migrants and our logo of course.

Target Market(s)

All around the world

Industry/Entity Type

Education

Font styles to use
Sans Serif

Colors

Designer to choose colors to be used in the design.

Requirements
Must have
• It needs to be designed well with relevant NZ images, international students/migrants and our logo of course.
Nice to have
• Copyright free images.
Should not have
• Images with any copyright issues.

```html
<!DOCTYPE html>
<html lang="en">
<head>
<meta charset="utf-8">
<title>Kowhai Pathways – Partnership Proposal</title>
<link href="https://fonts.googleapis.com/css2?family=Roboto:wght@400;500;700&family=Jost:wght@500&display=swap" rel="stylesheet">
<style>
:root{
  --backdrop:#b4b4b4;
  --paper:#ffffff;
  --lime:#d8f57c;
  --blue:#1c4f9c;
  --ink:#3a3a3a;
  --band:#efefe8;
  --ring:#e3ecf6;
}
*{margin:0;padding:0;box-sizing:border-box}
html,body{width:1200px;height:573px;overflow:hidden;background:var(--backdrop)}
body{position:relative;font-family:"Roboto",Arial,sans-serif;color:var(--ink)}
.page{position:absolute;top:48px;width:364px;height:470px;background:var(--paper);overflow:hidden}
.page--one{left:30px}
.page--two{left:423px}
.page--three{left:815px}
.abs{position:absolute}
.copy{font-size:5.5px;line-height:7.2px;color:var(--ink)}
.band-head{position:absolute;left:16px;width:332px;background:var(--band);font-size:5.8px;font-weight:700;color:#222;padding:2px 4px;border-left:2px solid var(--lime)}
.tick-head{display:flex;align-items:center;gap:3px;font-size:5.4px;font-weight:700;color:var(--blue)}
.tick-head svg{width:6px;height:6px;flex:none}
.rule{position:absolute;left:16px;right:0;height:3px;background:var(--blue)}

/* page one */
.hero-photo{left:16px;top:13px;width:332px;height:116px;background:linear-gradient(160deg,#8f9a92 0%,#5f6d68 45%,#a9b2a4 100%)}
.brand-panel{left:22px;top:30px;width:103px;height:100px;background:var(--lime);padding:8px 8px}
.brand-name{font-family:"Jost",Arial,sans-serif;font-weight:500;font-size:13px;color:#111;display:flex;align-items:center;gap:4px}
.brand-name i{display:inline-block;width:8px;height:8px;border-radius:50%;background:#111}
.brand-address{font-family:"Jost",Arial,sans-serif;font-weight:500;font-size:8.2px;line-height:10.2px;color:#111;margin-top:14px}
.doc-title{left:138px;top:135px;font-size:5.8px;font-weight:700;line-height:8px;color:#222}

/* page two */
.service-wheel{left:40px;top:24px}
.wheel-label{font-size:4.6px;font-weight:700;fill:var(--blue)}

/* page three */
.contact-head{left:16px;top:238px;width:332px;height:17px;background:var(--band);font-size:5.6px;font-weight:700;color:var(--blue);padding:5px 6px}
.contact-photo{left:16px;top:255px;width:332px;height:92px;background:linear-gradient(90deg,#f1ece6 0%,#e0b48e 45%,#d9d6d2 100%)}
.contact-brand{left:282px;top:265px;width:55px;height:26px;background:#fff;display:flex;align-items:center;justify-content:center;font-family:"Jost",Arial,sans-serif;font-weight:500;font-size:8px;color:#111}
.contact-card{left:16px;top:347px;width:126px;height:76px;background:var(--blue);padding:11px 8px;color:#fff}
.contact-row{display:flex;align-items:center;gap:4px;font-size:4.6px;line-height:6px;margin-bottom:6px}
.contact-row .dot{width:9px;height:9px;border-radius:50%;background:var(--lime);flex:none;display:flex;align-items:center;justify-content:center}
.contact-row .dot svg{width:5px;height:5px}
.contact-role{color:var(--lime);font-style:normal}
.street-photo{left:145px;top:347px;width:135px;height:76px;background:linear-gradient(180deg,#8fa4b8 0%,#c7ccd0 55%,#9aa0a4 100%)}
.campus-photo{left:283px;top:347px;width:65px;height:76px;background:linear-gradient(180deg,#9fc3e6 0%,#b9c9d6 40%,#6f7a58 100%)}
.footer-line{left:16px;top:440px;font-size:5.2px;font-weight:700;color:var(--blue)}
</style>
</head>
<body>

<svg width="0" height="0" style="position:absolute" aria-hidden="true">
  <symbol id="tick" viewBox="0 0 10 10"><circle cx="5" cy="5" r="5" fill="#1c4f9c"/><path d="M2.7 5.2l1.6 1.6 3-3.3" stroke="#fff" stroke-width="1.3" fill="none"/></symbol>
</svg>

<!-- Page one -->
<section class="page page--one">
  <div class="abs hero-photo" role="img" aria-label="Modern glass university building with native trees in New Zealand"></div>
  <div class="abs brand-panel">
    <div class="brand-name"><i></i>Kowhai</div>
    <p class="brand-address">Kowhai Pathways Ltd, 214 Riverbank Lane, Hillcrest, Hamilton, New Zealand – 3216.</p>
  </div>
  <h1 class="abs doc-title">NEW ZEALAND EDUCATION &amp; MIGRATION BUSINESS OPPORTUNITY<br>PARTNERSHIP PROPOSAL</h1>

  <h2 class="band-head" style="top:160px">Why New Zealand and who is Kowhai?</h2>
  <p class="abs copy" style="left:16px;top:172px;width:332px">New Zealand is booming as an education &amp; migration destination. In a world that is spiralling out of control; the serenity, safety and opportunities of New Zealand are attracting people from everywhere like a magnet. Numbers have been growing dramatically year on year. We are a deeply committed New Zealand education &amp; migration company, seeking to attract the best talent from around the world to make New Zealand their new home.</p>

  <h2 class="band-head" style="top:214px">Why collaborate with Kowhai?</h2>
  <p class="abs copy" style="left:16px;top:226px;width:332px">Collaborations can accelerate mutual growth in a globalised world. Our rationale in this proposal is that we do not have the reach in your market and vice versa you do not have a presence or team in New Zealand to continue to service your students or clients once they arrive here. By coming together we can achieve both these mutual objectives and create a viable and mutual business opportunity.</p>

  <h2 class="band-head" style="top:268px">What is the Kowhai partnership framework?</h2>
  <p class="abs copy" style="left:16px;top:280px;width:332px">We propose to work with you as our Referral Partner. A partnership that can be mutually beneficial and enhance the value of international education &amp; migration to deserving students and clients from everywhere. Our levels of association can vary depending on your current focus and how you can utilise our position especially in the areas of services that can only be rendered by a Licensed Immigration Adviser.</p>

  <h2 class="band-head" style="top:323px">What are the highlights of Kowhai?</h2>
  <div class="abs tick-head" style="left:16px;top:338px"><svg><use href="#tick"/></svg>We are New Zealand owned and based:</div>
  <p class="abs copy" style="left:16px;top:347px;width:332px">Hence we are able to provide services to clients in an end-to-end fashion from suggesting the right courses at the very beginning of their journey to hand-holding them all the way to employment and eventual residency in New Zealand. By working with us you not only create a viable business opportunity but can also be assured that your students/clients are in safe hands after they reach New Zealand. This is where the real challenges start for these young people as they need a huge amount of onshore support and guidance which we can provide.</p>
  <div class="abs tick-head" style="left:16px;top:395px"><svg><use href="#tick"/></svg>We have the full range of institutions:</div>
  <p class="abs copy" style="left:16px;top:404px;width:332px">We represent the entire gamut of quality New Zealand institutions and in the event your student needs/deserves the appropriate institution to fulfil their future aspirations, we can provide this opportunity for them together. We believe each student deserves to be in the institution that best serves their future interests and we can provide this opportunity for them.</p>
</section>

<!-- Page two -->
<section class="page page--two">
  <div class="rule" style="top:17px"></div>
  <svg class="abs service-wheel" width="280" height="160" viewBox="40 24 280 160" aria-label="Services: Tour, Skill Migration, Job and Migration, Study and settle in, Business migration, Investment Migration">
    <circle cx="182" cy="104" r="70" fill="var(--ring)"/>
    <circle cx="182" cy="104" r="62" fill="#fff"/>
    <circle cx="182" cy="104" r="56" fill="#7d6a5a" role="img" aria-label="International student studying with books and a plant"/>
    <g>
      <circle cx="158" cy="42" r="16" fill="var(--lime)"/><use href="#tick" x="154" y="38" width="8" height="8"/>
      <circle cx="220" cy="54" r="11" fill="var(--lime)"/><use href="#tick" x="216.5" y="50.5" width="7" height="7"/>
      <circle cx="233" cy="106" r="16" fill="var(--lime)"/><use href="#tick" x="229" y="102" width="8" height="8"/>
      <circle cx="182" cy="150" r="16" fill="var(--lime)"/><use href="#tick" x="178" y="146" width="8" height="8"/>
      <circle cx="140" cy="132" r="9" fill="var(--lime)"/><use href="#tick" x="136.5" y="128.5" width="7" height="7"/>
      <circle cx="125" cy="96" r="11" fill="var(--lime)"/><use href="#tick" x="121.5" y="92.5" width="7" height="7"/>
    </g>
    <text class="wheel-label" x="128" y="44">Tour</text>
    <text class="wheel-label" x="234" y="51">Skill Migration</text>
    <text class="wheel-label" x="251" y="108">Job and Migration</text>
    <text class="wheel-label" x="162" y="176">Study and settle in</text>
    <text class="wheel-label" x="84" y="138">Business migration</text>
    <text class="wheel-label" x="58" y="99">Investment Migration</text>
  </svg>

  <div class="abs tick-head" style="left:16px;top:195px"><svg><use href="#tick"/></svg>We have an experienced team and great software:</div>
  <p class="abs copy" style="left:24px;top:204px;width:324px">Our competent counseling team backed by a visa team (including ex- New Zealand immigration officers) will ensure that each student is matched to the right course, college, city and to a career of his choice. Your student's parents will be extremely satisfied since their child will be taken care of in a professional manner. We have also built our inhouse software to streamline all processes and partners will have access to their own login for management of their prospects. Not to forget our impressive Board of Advisers who are senior ex- NZ government officials and professionals.</p>

  <div class="abs tick-head" style="left:16px;top:270px"><svg><use href="#tick"/></svg>We have a very high visa success rate:</div>
  <p class="abs copy" style="left:24px;top:279px;width:324px">Our current visa success rate for the first quarter of 2018 sits well above 90% and we aim to maintain this and keep improving on it successfully. Last year it was 80%. As you are aware a visa process is a detailed legal matter, our processes will ensure that your students have a very high chance of success in their visa applications. This means you can focus on your core strength as a marketer and garner prospective students and leave the admission and visa process to an established and successful team.</p>

  <div class="abs tick-head" style="left:16px;top:335px"><svg><use href="#tick"/></svg>We have a legal license for all visa types:</div>
  <p class="abs copy" style="left:24px;top:344px;width:324px">We are headed by a Licensed immigration Adviser based in New Zealand who was also an IAA Reference Group member for 2017. Our Senior Team members are also getting upgraded towards acquiring their own immigration license. Hence we can assist in all visa types legally. Those without a license simply cannot. For instance international students will need a licensed adviser for their spouse and children visa. We can provide that and this will enable you to gain maximum mileage in your market as someone who can provide a full solution to the entire family.</p>

  <div class="abs tick-head" style="left:16px;top:401px"><svg><use href="#tick"/></svg>We are present at every step onshore for clients:</div>
  <p class="abs copy" style="left:24px;top:410px;width:324px">We also provide our students and clients with onshore support. Our local team in NZ will guide them with various options for airport pickup, accommodation and part-time job opportunities. Apart from giving ongoing immigration advice during a student's period of stay, we have also been organising a lot of fun activities like networking dinners, picnics and other events. Thus they are assured of a smooth transition towards an eventual NZ residency.</p>
</section>

<!-- Page three -->
<section class="page page--three">
  <div class="rule" style="top:10px"></div>

  <div class="abs tick-head" style="left:16px;top:24px"><svg><use href="#tick"/></svg>We are transparent and honest to the core:</div>
  <p class="abs copy" style="left:24px;top:33px;width:324px">Our operating principle is to do good to New Zealand, our clients, our partners, our employees and our shareholders in that order. We believe our primary goal is to create a better society in New Zealand and hence we desist from any practice that will hurt this principle. We consistently uphold the integrity of the immigration process of the country and are brutally honest with all stakeholders. Which means you will be partnering with a company that has a zero tolerance for fake documents or clients. As regards money matters too we are fully transparent and none of our partners will ever be given a raw deal.</p>

  <div class="abs tick-head" style="left:16px;top:96px"><svg><use href="#tick"/></svg>We are growing and adding new products:</div>
  <p class="abs copy" style="left:24px;top:105px;width:324px">At the moment we are only focusing on New Zealand education &amp; migration, but in the coming years we intend to add New Zealand employment, business, investment and tourism opportunities as well. As and when these new products are launched all our existing partner will get the opportunity to refer clients for these too. This means additional revenue to you and an increase in your portfolio of products.</p>

  <div class="abs tick-head" style="left:16px;top:149px"><svg><use href="#tick"/></svg>How do we take this forward with Kowhai?</div>
  <p class="abs copy" style="left:24px;top:158px;width:324px">Simple. If you like what you have read so far, respond to our initial mail and our Team Leader – Business Development will revert with a commercial proposal. That can be discussed and once agreeable to both parties we will sign the agreement and proceed to the next stage. This will include training of your staff where needed and initiating other processes.</p>
  <p class="abs copy" style="left:24px;top:202px;width:324px">We look forward to working with you.<br>Haere mai ki Kowhai whanau! Welcome to the Kowhai Family!</p>

  <div class="abs contact-head">For more information, please contact:</div>
  <div class="abs contact-photo" role="img" aria-label="Student thinking with a pencil at a bright desk"></div>
  <div class="abs contact-brand">Kowhai</div>
  <div class="abs contact-card">
    <div class="contact-row"><span class="dot"><svg viewBox="0 0 10 10"><circle cx="5" cy="3.2" r="2" fill="#1c4f9c"/><path d="M1.5 9.5a3.5 3.5 0 0 1 7 0z" fill="#1c4f9c"/></svg></span><span>Ms Tara Wilcox<br><em class="contact-role">Team Leader – Business Development</em></span></div>
    <div class="contact-row"><span class="dot"><svg viewBox="0 0 10 10"><rect x="1" y="2.5" width="8" height="5" fill="none" stroke="#1c4f9c" stroke-width="1"/><path d="M1 2.5l4 3 4-3" fill="none" stroke="#1c4f9c" stroke-width="1"/></svg></span><span>Email: tara.wilcox@kowhai.kiwi</span></div>
    <div class="contact-row"><span class="dot"><svg viewBox="0 0 10 10"><path d="M2.5 1l2 2-1 1.3a6 6 0 0 0 2.2 2.2L7 5.5l2 2-1.3 1.5C4.5 9 1 5.5 1 2.3z" fill="#1c4f9c"/></svg></span><span>Phone: +91-9000012345</span></div>
  </div>
  <div class="abs street-photo" role="img" aria-label="Student sitting on a city street"></div>
  <div class="abs campus-photo" role="img" aria-label="Historic stone university clock tower"></div>

  <p class="abs footer-line">© 2018 | Kowhai Pathways Ltd | Privacy Policy | All Rights Reserved</p>
</section>

</body>
</html>
```